Forest Consultant/Timber Buyer needs a clean business card

We are a forestry consulting and timber buying company. We meet with private landowners and assist them with timber management and timber harvesting. We would like a professional business card, please no clip art. logo is blue and white but would like to see a gray,silver, or some other color incorporated. Would like basic contact info. Would like to the layout to be creative and sleek but masculine.

Target Market(s)

private landowners

Industry/Entity Type

Business

Contact Information for Business Card

name,position, cell number, office number, email, website. This might be to cluttered. Basic contact info is what we are looking for.

Contact info can all be on one side with logo on the other.

Font styles to use
Serif
Sans Serif

Colors
0255a3
ffffff
aaaaaa

Requirements
Must have
• We just want it professional.
Nice to have
• Creative layout.
Should not have
• please no clip art of log trucks etc.

```html
<!DOCTYPE html>
<html lang="en">
<head>
<meta charset="utf-8">
<title>Harlow Land &amp; Timber – Business Card</title>
<link href="https://fonts.googleapis.com/css2?family=Lato:wght@400;700&display=swap" rel="stylesheet">
<style>
  :root {
    --brand-blue: #0255a3;
    --paper: #ffffff;
    --silver: #aaaaaa;
    --ink: #1d1d1d;
    --backdrop: #e6e7e9;
    --watermark: #f2f3f5;
  }
  * { box-sizing: border-box; margin: 0; padding: 0; }
  html, body {
    width: 1200px; height: 900px; overflow: hidden;
    background: var(--backdrop);
    font-family: "Lato", Arial, sans-serif;
  }
  .canvas { position: relative; width: 1200px; height: 900px; }
  .card {
    position: absolute; left: 250px; width: 700px; height: 400px;
    overflow: hidden;
    box-shadow: 0 6px 18px rgba(0,0,0,0.18);
  }
  .card--front { top: 40px; background: var(--brand-blue); color: var(--paper); }
  .card--back { top: 460px; background: var(--paper); color: var(--ink); }

  .brand { display: flex; align-items: center; gap: 18px; }
  .brand__dot {
    width: 58px; height: 58px; border-radius: 50%;
    border: 5px solid currentColor; flex: none;
  }
  .brand__name {
    font-weight: 700; font-size: 40px; letter-spacing: 3px;
    line-height: 1; text-transform: uppercase;
  }
  .brand__name small {
    display: block; font-size: 15px; letter-spacing: 7px; margin-top: 8px;
  }

  .card--front .brand { position: absolute; left: 150px; top: 120px; }
  .front__url {
    position: absolute; left: 0; right: 0; top: 300px;
    text-align: center; font-size: 19px; letter-spacing: 3px;
  }

  .card--back .brand { position: absolute; left: 50px; top: 44px; color: var(--brand-blue); }
  .brand--back .brand__name { font-size: 34px; }
  .brand--back .brand__dot { width: 50px; height: 50px; border-width: 4px; }

  .watermark {
    position: absolute; left: 380px; top: 110px;
    width: 340px; height: 340px; border-radius: 50%;
    border: 22px solid var(--watermark);
  }

  .contact { position: absolute; left: 50px; top: 150px; font-size: 18px; line-height: 1.35; }
  .contact__address { margin-bottom: 12px; }
  .contact__list { list-style: none; }
  .contact__list li { display: flex; align-items: center; gap: 12px; height: 27px; }
  .contact__list svg { width: 16px; height: 16px; fill: var(--brand-blue); flex: none; }

  .person { position: absolute; right: 70px; top: 250px; text-align: left; }
  .person__name { color: var(--brand-blue); font-size: 32px; font-weight: 400; }
  .person__role { font-size: 19px; margin-top: 2px; }

  .band {
    position: absolute; left: 0; right: 0; bottom: 0; height: 14px;
    background: var(--brand-blue);
    border-top: 3px solid var(--silver);
  }
</style>
</head>
<body>
<main class="canvas">

  <section class="card card--front" aria-label="Card front">
    <div class="brand">
      <span class="brand__dot" aria-hidden="true"></span>
      <p class="brand__name">Harlow<small>Land &amp; Timber</small></p>
    </div>
    <p class="front__url">www.harlowtimber.com</p>
  </section>

  <section class="card card--back" aria-label="Card back">
    <div class="watermark" aria-hidden="true"></div>

    <div class="brand brand--back">
      <span class="brand__dot" aria-hidden="true"></span>
      <p class="brand__name">Harlow<small>Land &amp; Timber</small></p>
    </div>

    <div class="contact">
      <p class="contact__address">1450 Pine Ridge Rd<br>Lufkin TX 75901</p>
      <ul class="contact__list">
        <li>
          <svg viewBox="0 0 16 16" aria-hidden="true"><path d="M3 1l3 3-1.5 2a9 9 0 0 0 5.5 5.5L12 10l3 3-2 2C6 15 1 10 1 3z"/></svg>
          936 555 0140
        </li>
        <li>
          <svg viewBox="0 0 16 16" aria-hidden="true"><path d="M4 1h8v4H4zM1 6h14v7h-3v2H4v-2H1zM5 10v4h6v-4z"/></svg>
          936 555 0141
        </li>
        <li>
          <svg viewBox="0 0 16 16" aria-hidden="true"><path d="M1 3h14v1L8 9 1 4zM1 6l7 5 7-5v7H1z"/></svg>
          info@harlowtimber.com
        </li>
        <li>
          <svg viewBox="0 0 16 16" aria-hidden="true"><path d="M8 1a7 7 0 1 0 0 14A7 7 0 0 0 8 1zm0 1.5c1 1 1.7 2.8 1.8 4.7H6.2C6.3 5.3 7 3.5 8 2.5zM2.6 7.2h2.3c.1-1.7.5-3.2 1.2-4.3A5.6 5.6 0 0 0 2.6 7.2zm0 1.6a5.6 5.6 0 0 0 3.5 4.3C5.4 12 5 10.5 4.9 8.8zm3.6 0h3.6c-.1 1.9-.8 3.7-1.8 4.7-1-1-1.7-2.8-1.8-4.7zm4.9 0c-.1 1.7-.5 3.2-1.2 4.3a5.6 5.6 0 0 0 3.5-4.3zm2.3-1.6a5.6 5.6 0 0 0-3.5-4.3c.7 1.1 1.1 2.6 1.2 4.3z"/></svg>
          www.harlowtimber.com
        </li>
      </ul>
    </div>

    <div class="person">
      <p class="person__name">Dale Whitford</p>
      <p class="person__role">Manager</p>
    </div>

    <div class="band" aria-hidden="true"></div>
  </section>

</main>
</body>
</html>
```